Professional business cards for real estate development company

I need business cards for my new real estate development company. The company, "KORVA" is a real estate development, investment, and advisory firm with a focus on multifamily, office, and mixed-use projects across primary and secondary markets in the Southeast United States.

Style preference is modern

Industry/Entity Type

Real Estate Development

Contact Information for Business Card

The business cards need to include:
Name
Title
Mailing Address
Phone Number
Web Address

Logo is attached. I would like white to be the primary color with incorporation of the company colors: #232D3A and #B5A451

Font styles to use
Other font styles liked:
• Montserrat, Avenir

Requirements
Must have
• Company Logo. No need to include the company name since the name is in the logo.
Should not have
• No line type designs

```html
<!DOCTYPE html>
<html lang="en">
<head>
<meta charset="utf-8">
<title>KORVA business cards</title>
<link href="https://fonts.googleapis.com/css2?family=Montserrat:wght@500;600;700&family=Roboto:wght@400&display=swap" rel="stylesheet">
<style>
  :root {
    --navy: #232D3A;
    --gold: #B5A451;
    --white: #FFFFFF;
    --ink: #2A2F38;
    --muted: #5B6068;
    --backdrop: #1C1D21;
  }
  * { box-sizing: border-box; margin: 0; padding: 0; }
  html, body { width: 1200px; height: 786px; overflow: hidden; }
  body {
    background: var(--backdrop);
    display: flex;
    align-items: center;
    justify-content: center;
    gap: 40px;
    font-family: "Roboto", Arial, sans-serif;
  }
  .card {
    position: relative;
    width: 540px;
    height: 309px;
    border-radius: 2px;
    overflow: hidden;
  }
  .card--front {
    background: var(--navy);
    display: flex;
    align-items: center;
    justify-content: center;
  }
  .card--back { background: var(--white); }

  .wordmark {
    display: flex;
    align-items: center;
    gap: 12px;
    font-family: "Montserrat", Arial, sans-serif;
    font-weight: 600;
    letter-spacing: 4px;
  }
  .wordmark__square { border: 2px solid currentColor; }
  .card--front .wordmark { color: #C9CDD3; font-size: 52px; }
  .card--front .wordmark__square { width: 40px; height: 40px; }
  .card--back .wordmark {
    position: absolute;
    top: 40px;
    right: 44px;
    color: var(--navy);
    font-size: 34px;
    gap: 9px;
  }
  .card--back .wordmark__square { width: 26px; height: 26px; }

  .holder {
    position: absolute;
    left: 40px;
    top: 150px;
  }
  .holder__name {
    font-family: "Montserrat", Arial, sans-serif;
    font-weight: 700;
    font-size: 17px;
    color: var(--ink);
    white-space: nowrap;
  }
  .holder__title {
    font-family: "Montserrat", Arial, sans-serif;
    font-weight: 600;
    font-size: 13px;
    color: var(--gold);
    margin-top: 2px;
  }

  .contact {
    position: absolute;
    left: 40px;
    top: 206px;
    list-style: none;
    font-size: 12.5px;
    color: var(--muted);
  }
  .contact li { display: flex; align-items: center; gap: 8px; height: 19px; white-space: nowrap; }
  .contact svg { width: 11px; height: 11px; flex: none; }

  .edge-mark {
    position: absolute;
    left: 0;
    top: 205px;
    width: 18px;
    height: 20px;
    background: var(--navy);
  }
</style>
</head>
<body>
  <section class="card card--front" aria-label="Card front">
    <div class="wordmark"><span class="wordmark__square"></span>KORVA</div>
  </section>

  <section class="card card--back" aria-label="Card back">
    <div class="wordmark"><span class="wordmark__square"></span>KORVA</div>

    <div class="holder">
      <p class="holder__name">DANA WHITCOMBE</p>
      <p class="holder__title">President</p>
    </div>

    <span class="edge-mark"></span>

    <ul class="contact">
      <li>
        <svg viewBox="0 0 12 12" aria-hidden="true"><circle cx="6" cy="6" r="6" fill="#232D3A"/><path d="M3.6 3.2l1.2-.4.7 1.6-.8.6c.4.9 1 1.5 1.9 1.9l.6-.8 1.6.7-.4 1.2c-2.6-.2-4.6-2.2-4.8-4.8z" fill="#fff"/></svg>
        +14045550187
      </li>
      <li>
        <svg viewBox="0 0 12 12" aria-hidden="true"><circle cx="6" cy="6" r="6" fill="#232D3A"/><rect x="3" y="4" width="6" height="4.2" fill="none" stroke="#fff" stroke-width=".9"/><path d="M3 4l3 2.3L9 4" fill="none" stroke="#fff" stroke-width=".9"/></svg>
        dwhitcombe@korvadevelopment.com
      </li>
      <li>
        <svg viewBox="0 0 12 12" aria-hidden="true"><circle cx="6" cy="6" r="6" fill="#232D3A"/><circle cx="6" cy="6" r="3" fill="none" stroke="#fff" stroke-width=".8"/><ellipse cx="6" cy="6" rx="1.2" ry="3" fill="none" stroke="#fff" stroke-width=".8"/><path d="M3 6h6" stroke="#fff" stroke-width=".8"/></svg>
        www.korvadevelopment.com
      </li>
      <li>
        <svg viewBox="0 0 12 12" aria-hidden="true"><circle cx="6" cy="6" r="6" fill="#232D3A"/><path d="M6 9.4C4.6 7.7 3.8 6.5 3.8 5.3a2.2 2.2 0 0 1 4.4 0c0 1.2-.8 2.4-2.2 4.1z" fill="#fff"/><circle cx="6" cy="5.3" r=".8" fill="#232D3A"/></svg>
        PO Box 4821, Charlotte, NC 28202
      </li>
    </ul>
  </section>
</body>
</html>
```